Sleek, Professional Business Card Design Needed

Business Cards - Logo Attached.

We are a solar consulting company. We are national and want our cards to represent the professional high quality products that we offer.

Industry/Entity Type

Business

Contact Information for Business Card

n/a

Requirements
Must have
• Design
• Name
• Position
• Number
• Email
• Address
Should not have
• Not be too crowded

```html
<!DOCTYPE html>
<html lang="en">
<head>
<meta charset="utf-8">
<title>Sunward Energy – Business Card</title>
<link rel="stylesheet" href="https://fonts.googleapis.com/css2?family=Jost:wght@400;500&display=swap">
<style>
  :root {
    --brand-blue: #0a8fcd;
    --brand-green: #a3cd3b;
    --paper: #ffffff;
  }
  html, body {
    margin: 0;
    padding: 0;
    overflow: hidden;
    background: var(--paper);
  }
  .card {
    position: relative;
    width: 686px;
    height: 1200px;
    background: var(--paper);
    font-family: "Jost", "Futura", sans-serif;
    overflow: hidden;
  }
  .brand {
    position: absolute;
    top: 72px;
    left: 0;
    width: 100%;
    text-align: center;
  }
  .brand-mark {
    display: block;
    margin: 0 auto;
  }
  .brand-name {
    margin: 22px 0 0;
    font-size: 60px;
    font-weight: 500;
    letter-spacing: 1px;
    line-height: 1;
    color: var(--brand-blue);
  }
  .band {
    position: absolute;
    left: 0;
    width: 100%;
    display: flex;
    align-items: center;
    justify-content: center;
    margin: 0;
    font-weight: 500;
  }
  .band--name {
    top: 526px;
    height: 57px;
    background: var(--brand-blue);
    color: var(--brand-green);
    font-size: 48px;
  }
  .band--position {
    top: 606px;
    height: 52px;
    background: var(--brand-green);
    color: var(--brand-blue);
    font-size: 37px;
  }
  .contact {
    position: absolute;
    left: 0;
    width: 100%;
    margin: 0;
    text-align: center;
    font-weight: 400;
  }
  .contact--address {
    top: 756px;
    font-size: 38px;
    line-height: 46px;
    color: var(--brand-blue);
  }
  .contact--phone {
    top: 990px;
    font-size: 37px;
    color: var(--brand-green);
  }
  .contact--email {
    top: 1102px;
    font-size: 34px;
    font-weight: 500;
    color: var(--brand-blue);
  }
</style>
</head>
<body>
  <main class="card">
    <header class="brand">
      <svg class="brand-mark" width="200" height="200" viewBox="0 0 200 200" aria-hidden="true">
        <circle cx="100" cy="100" r="88" fill="none" stroke="var(--brand-blue)" stroke-width="18"/>
      </svg>
      <p class="brand-name">SUNWARD ENERGY</p>
    </header>

    <h1 class="band band--name">Name</h1>
    <h2 class="band band--position">Position</h2>

    <address class="contact contact--address">
      Address:XXXXXXXXXXX<br>
      XXXXXXXXXXXXXXXXXX<br>
      XXXXXXXXXXXXXXXXXX
    </address>

    <p class="contact contact--phone">XXX.XXX.XXXX</p>
    <p class="contact contact--email">Email: XXXXXXXXX@xxxxxxx.com</p>
  </main>
</body>
</html>
```